Sorpresa para un amigo
Zielgruppe
Tito, un español simpático de 32 años
Aufgabenstellung
Hola, soy Torsten, uno de los fundadores de quelvento.
Tres semanas antes he llevado el Camino de Santiago en España en la bicicleta y tengo con esto Tito, un español muy simpático de modo conocido. Hemos llevado en común aproximadamente 700 kilómetros y hemos vivido mucho juntos.
Tito tiene el 2 de julio el cumpleaños y quisiera sorprenderlo. Por favor, una tarjeta de cumpleaños hermosa forma para él, tenemos un recuerdo hermoso de Camino.
Podéis usar una de las fotos de las colocaciones e incorporar quizá algunas nuestras citas el más con mucho gusto:
¡Tiempo mal!
¡El culo mal!
¡La rodilla mal!
¿Cómo lejos todavía hasta Santiago?
La tarjeta debe ser expedida como E-Mail

```html
<!DOCTYPE html>
<html lang="es">
<head>
<meta charset="utf-8">
<title>Felicidades Tito</title>
<link rel="stylesheet" href="https://fonts.googleapis.com/css2?family=Caveat:wght@500&family=Varela+Round&family=Arimo:wght@700&display=swap">
<style>
  :root {
    --paper: #ffffff;
    --film: #0b0b0b;
    --hole: #e9e9e9;
    --edge-mark: #f2e23a;
    --ink-red: #e0262b;
    --shadow: #8a8a8a;
  }
  html, body {
    margin: 0;
    padding: 0;
    width: 1200px;
    height: 560px;
    overflow: hidden;
    background: var(--paper);
  }
  .card {
    position: relative;
    width: 1200px;
    height: 560px;
  }
  .card svg { display: block; }
  .question {
    font-family: "Caveat", cursive;
    font-size: 24px;
    fill: var(--ink-red);
  }
  .edge-label {
    font-family: "Arimo", Arial, sans-serif;
    font-size: 10px;
    fill: var(--edge-mark);
  }
  .edge-number {
    font-family: "Arimo", Arial, sans-serif;
    font-size: 13px;
    fill: var(--edge-mark);
  }
  .complaints {
    font-family: "Varela Round", sans-serif;
    font-size: 20px;
    fill: var(--ink-red);
  }
  .strip { fill: var(--film); }
  .sprocket { fill: var(--hole); }
  .strip-shadow { fill: var(--shadow); opacity: .55; }
  .frame-blank { fill: var(--paper); }
</style>
</head>
<body>
<main class="card">
  <svg width="1200" height="560" viewBox="0 0 1200 560" xmlns="http://www.w3.org/2000/svg">
    <defs>
      <filter id="soft-blur" x="-5%" y="-20%" width="110%" height="140%">
        <feGaussianBlur stdDeviation="7"/>
      </filter>
      <pattern id="sprocket-row" x="20" y="0" width="52" height="560" patternUnits="userSpaceOnUse">
        <rect class="sprocket" x="0" y="196" width="17" height="22" rx="3"/>
        <rect class="sprocket" x="0" y="364" width="17" height="22" rx="3"/>
      </pattern>
      <linearGradient id="tone-hills" x1="0" y1="0" x2="0" y2="1">
        <stop offset="0" stop-color="#c9d3dc"/>
        <stop offset=".45" stop-color="#a7b39a"/>
        <stop offset="1" stop-color="#6f7a4a"/>
      </linearGradient>
      <linearGradient id="tone-cathedral" x1="0" y1="0" x2="0" y2="1">
        <stop offset="0" stop-color="#b9b5ad"/>
        <stop offset=".5" stop-color="#8a7358"/>
        <stop offset="1" stop-color="#5a4838"/>
      </linearGradient>
    </defs>

    <text class="question" x="425" y="158" transform="rotate(-5 425 158)">falta mucho para Santiago??</text>

    <rect class="strip-shadow" x="10" y="395" width="1120" height="26" filter="url(#soft-blur)"/>

    <g class="film-strip">
      <rect class="strip" x="0" y="177" width="1125" height="227"/>
      <rect x="0" y="177" width="1125" height="227" fill="url(#sprocket-row)"/>

      <g class="edge-top">
        <text class="edge-number" x="140" y="193">1</text>
        <text class="edge-label" x="232" y="191">FELICIDADES TITO</text>
        <text class="edge-number" x="399" y="193">2</text>
        <text class="edge-label" x="490" y="191">FELICIDADES TITO</text>
        <text class="edge-number" x="659" y="193">3</text>
        <text class="edge-label" x="752" y="191">FELICIDADES TITO</text>
        <text class="edge-number" x="920" y="193">4</text>
        <text class="edge-label" x="1014" y="191">FELICIDADES TITO</text>
      </g>

      <g class="edge-bottom">
        <text class="edge-number" x="140" y="399">1</text>
        <text class="edge-label" x="232" y="398">→1A</text>
        <text class="edge-number" x="399" y="399">2</text>
        <text class="edge-label" x="492" y="398">→2A</text>
        <text class="edge-number" x="659" y="399">3</text>
        <text class="edge-label" x="752" y="398">→3A</text>
        <text class="edge-number" x="920" y="399">4</text>
        <text class="edge-label" x="1014" y="398">→4A</text>
      </g>

      <g class="frame photo" role="img" aria-label="Foto: los dos ciclistas juntos en el Camino, con campos y colinas detrás">
        <rect x="0" y="225" width="225" height="133" fill="url(#tone-hills)"/>
      </g>
      <g class="frame photo" role="img" aria-label="Foto: los dos amigos con sus bicis en un alto del Camino, paisaje de campos verdes">
        <rect x="240" y="225" width="248" height="133" fill="url(#tone-hills)"/>
      </g>
      <g class="frame photo" role="img" aria-label="Foto: fachada de la catedral de Santiago de Compostela">
        <rect x="500" y="225" width="246" height="133" fill="url(#tone-cathedral)"/>
      </g>
      <g class="frame note">
        <rect class="frame-blank" x="759" y="225" width="247" height="133"/>
        <text class="complaints" x="777" y="262">el tiempo.... maaaal</text>
        <text class="complaints" x="777" y="286">el culo.............. maaaal</text>
        <text class="complaints" x="777" y="310">y la rodilla.........maaaal</text>
      </g>
      <g class="frame photo" role="img" aria-label="Foto: los dos amigos de pie en lo alto de una colina">
        <rect x="1020" y="225" width="105" height="133" fill="url(#tone-hills)"/>
      </g>
    </g>
  </svg>
</main>
</body>
</html>
```